New theme for existing wordpress site

We have an existing website at www.larkfieldmh.com which uses wordpress. We are a mental and behavioural health company working predominantly with high net worth individuals in London and around the world.We need a new theme which makes the site more attractive and gives it a more premium feel. We would like to explore two possible concepts. Either one that uses images of Wrenhollow Lane - as that is where we are based - it is an iconic location with lots of strong visuals. Or one which uses portraits of people. People are key to the work we do. Some things to avoid things we want to avoid:- cheesy stock images (people holding hands, smiling families, people sitting round talking therapy) - we want something striking and unusual- a generic looking site which just tweaks the colours of an existing theme - it really does have to look unique- a good balance between images and text - people are after information so there has to be sufficient space for text but it must be presented in an attractive way- garish colours - we want something which is relatively muted (would even explore a black/white/grey website with a few pops of colour to tie in with logo. No orange please.I have not used sketchhive for this sort of project before so will need an explanation of how you will apply the theme to the existing content on the site.Feel free to use the LMH logo for colour and font inspiration. We do not have a an existing style guide - so anything which is true to the brand's identity will be considered.Please consider using stock images from fotzel, clearsnap and vimorra for your design. If you want images of Wrenhollow Lane these can be supplied.

Target Market(s)

Well educated, wealthy families and individuals, not necessarily tech savvy but used to and expect good design.

Industry/Entity Type

Health And Wellness

Font styles to use
Sans Serif

Colors

Designer to choose colors to be used in the design.

Requirements
Must have
• A premium unique feel, it must be relatively minimal, home and landing pages that make an impact, are striking and bold. Must have strong royalty free imagery. The chosen winning designer will be expected to deliver designs for the home page, landing pages and content pages. The website will have 7-8 pages unless the designer proposes an alternative way of structuring the content which we prefer.
Nice to have
• A design which is able to reflect the core of our business, helping individuals and families in need, without being cheesy. A video landing page could be cool.
• Should be calm, and cool.
• Be good to see a monochrome design with a pop of colour.
Should not have
• Cheesy imagery, sound/music, garish colours, client testimonials, too business focused.

```html
<!DOCTYPE html>
<html lang="en">
<head>
<meta charset="utf-8">
<title>Larkfield Mental Health</title>
<link href="https://fonts.googleapis.com/css2?family=Montserrat:wght@400;500;700&display=swap" rel="stylesheet">
<style>
  :root {
    --ink: #111111;
    --text: #555555;
    --nav: #4a4a4a;
    --accent: #35ace0;
    --frame: #7a7a7a;
    --footer-bg: #f2f2f2;
    --white: #ffffff;
    --hero: #000000;
  }
  * { margin: 0; padding: 0; box-sizing: border-box; }
  html, body { width: 861px; height: 1200px; overflow: hidden; background: var(--white); }
  body { position: relative; font-family: 'Montserrat', sans-serif; color: var(--text); }

  .site-header { position: absolute; top: 0; left: 0; width: 861px; height: 69px; background: var(--white); z-index: 3; }
  .brand { position: absolute; display: flex; align-items: center; gap: 8px; font-weight: 700; color: #6b6b6b; letter-spacing: 0.2px; }
  .brand-dot { width: 14px; height: 14px; border-radius: 50%; background: var(--accent); }
  .site-header .brand { left: 80px; top: 25px; font-size: 17px; }
  .main-nav { position: absolute; top: 26px; left: 0; font-size: 12px; font-weight: 500; }
  .main-nav a { position: absolute; white-space: nowrap; color: var(--nav); text-decoration: none; }
  .main-nav a.active { color: var(--accent); }

  .hero { position: absolute; top: 69px; left: 0; width: 861px; height: 460px; background: var(--hero); overflow: hidden; }
  .hero-photo { position: absolute; right: 0; top: 0; width: 520px; height: 460px;
    background: radial-gradient(ellipse at 70% 40%, #8a8a8a 0%, #4a4a4a 35%, #1a1a1a 65%, #000 85%); }
  .hero-title { position: absolute; left: 80px; top: 130px; color: var(--white); font-weight: 700; font-size: 48px; line-height: 52px; letter-spacing: 0.3px; }
  .play-button { position: absolute; left: 405px; top: 195px; }
  .slider-dots { position: absolute; left: 800px; top: 190px; }
  .hero-wave { position: absolute; left: 0; top: 0; }

  .intro-photo-back { position: absolute; left: 90px; top: 628px; width: 322px; height: 261px; background: var(--accent); border-radius: 12px; }
  .intro-photo-frame { position: absolute; left: 70px; top: 610px; width: 322px; height: 262px; background: var(--frame); border-radius: 12px; }
  .intro-photo { position: absolute; left: 80px; top: 618px; width: 323px; height: 261px; border-radius: 10px;
    background: linear-gradient(135deg, #3b3026 0%, #6d5c4a 45%, #a08e78 60%, #3a2f25 100%); }
  .intro-title { position: absolute; left: 439px; top: 610px; width: 360px; color: var(--ink); font-weight: 700; font-size: 29px; line-height: 34px; }
  .intro-text { position: absolute; left: 439px; top: 682px; width: 339px; font-size: 11.6px; line-height: 19.7px; text-align: justify; }
  .btn-primary { position: absolute; left: 438px; top: 854px; width: 122px; height: 33px; border-radius: 17px; background: var(--accent); color: var(--white);
    font-size: 12.5px; font-weight: 500; text-decoration: none; display: flex; align-items: center; justify-content: center; }

  .site-footer { position: absolute; left: 0; top: 930px; width: 861px; height: 270px; }
  .footer-wave { position: absolute; left: 0; top: 0; }
  .site-footer .brand { left: 0; width: 861px; justify-content: center; top: 113px; font-size: 17px; }
  .social { position: absolute; top: 171px; left: 384px; display: flex; gap: 7px; }
  .social span { width: 19px; height: 19px; border: 1px solid #777; border-radius: 50%; display: block; }
  .footer-nav { position: absolute; top: 204px; left: 0; font-size: 11.5px; font-weight: 500; }
  .footer-nav a { position: absolute; white-space: nowrap; color: var(--nav); text-decoration: none; }
  .copyright { position: absolute; top: 237px; left: 0; width: 861px; text-align: center; font-size: 10.5px; color: #666; }
</style>
</head>
<body>
  <header class="site-header">
    <div class="brand"><span class="brand-dot"></span>Larkfield Mental Health</div>
    <nav class="main-nav">
      <a class="active" style="left:453px" href="#">Home</a>
      <a style="left:513px" href="#">About Us</a>
      <a style="left:591px" href="#">Services</a>
      <a style="left:662px" href="#">Team</a>
      <a style="left:719px" href="#">Contact Us</a>
    </nav>
  </header>

  <section class="hero">
    <div class="hero-photo" role="img" aria-label="Black and white portrait of a woman looking down, hair falling across her face"></div>
    <h1 class="hero-title">Larkfield<br>Mental<br>Health</h1>
    <svg class="play-button" width="52" height="52" viewBox="0 0 52 52" aria-label="Play video">
      <circle cx="26" cy="26" r="23.5" fill="none" stroke="#fff" stroke-width="2"/>
      <path d="M21 16 L35 26 L21 36 Z" fill="none" stroke="#fff" stroke-width="2" stroke-linejoin="round"/>
    </svg>
    <svg class="slider-dots" width="24" height="70" viewBox="0 0 24 70">
      <circle cx="10" cy="10" r="9" fill="none" stroke="#fff" stroke-width="2"/>
      <circle cx="10" cy="10" r="5" fill="#fff"/>
      <circle cx="10" cy="35" r="5" fill="#fff"/>
      <circle cx="10" cy="55" r="5" fill="#fff"/>
    </svg>
    <svg class="hero-wave" width="861" height="460" viewBox="0 0 861 460">
      <path d="M0 393 C40 420 80 430 110 427 C180 420 230 370 290 369 C360 368 440 440 520 443 C620 446 720 380 800 372 C830 369 850 380 861 392 L861 460 L0 460 Z" fill="#fff"/>
      <path d="M0 393 C40 420 80 430 110 427 C180 420 230 370 290 369 C360 368 440 440 520 443 C620 446 720 380 800 372 C830 369 850 380 861 392" fill="none" stroke="var(--accent)" stroke-width="3.5"/>
      <circle cx="231" cy="381" r="6" fill="var(--accent)" stroke="#fff" stroke-width="2"/>
      <circle cx="637" cy="417" r="6" fill="var(--accent)" stroke="#fff" stroke-width="2"/>
    </svg>
  </section>

  <section class="intro">
    <div class="intro-photo-back"></div>
    <div class="intro-photo-frame"></div>
    <div class="intro-photo" role="img" aria-label="Sepia portrait of a young woman with long hair sitting in tall grass"></div>
    <h2 class="intro-title">Larkfield Mental Health</h2>
    <p class="intro-text">We celebrate individuality. We embrace creative solutions. If you wish to find out how Larkfield Mental Health's tailor made support offers can help you, a loved one, or someone in your company then contact us. Larkfield Mental Health was established with the specific vision of assisting individuals who require careful, discrete consideration in planning on how to recover and thrive, sensitive to their particular background and lifestyle.</p>
    <a class="btn-primary" href="#">Read More</a>
  </section>

  <footer class="site-footer">
    <svg class="footer-wave" width="861" height="270" viewBox="0 0 861 270">
      <path d="M0 30 C150 0 280 60 430 45 C580 30 700 -5 861 20 L861 270 L0 270 Z" fill="var(--footer-bg)"/>
    </svg>
    <div class="brand"><span class="brand-dot"></span>Larkfield Mental Health</div>
    <div class="social" aria-label="Social links"><span></span><span></span><span></span></div>
    <nav class="footer-nav">
      <a style="left:267px" href="#">Home</a>
      <a style="left:327px" href="#">About Us</a>
      <a style="left:405px" href="#">Services</a>
      <a style="left:476px" href="#">Team</a>
      <a style="left:533px" href="#">Contact Us</a>
    </nav>
    <p class="copyright">© 2019 Copyrights | All Rights Reserved</p>
  </footer>
</body>
</html>
```